Bakery Replacement Lighted Sign Face

We are opening a new bakery that sells only cakes. The name is "The Willow Lantern." We are replacing the current sign face with a new look that states our name and makes a bold statement of fun. We will be known for having 101 cakes that are always ready for immediate pickup or delivery. Our colors are pink, orange, and lime green. An image is provided to see the colors.

Target Market(s)

people who buy cakes for parties and all other occasions

Industry/Entity Type

Cakes

Other font styles liked:
• look at the logo and file for the main font name

Colors
59FF00
82FF00
B8FF75
E3FFCB
F4FFEA
F0912C
F2A743
F7CA91
FBE8D2
FDF5EE
EB3D1F
EC4F4E
F09395
F8D3D4
FCEDEE

Requirements
Must have
• The name of the bakery. Logo can be used as is or changed as shown in one of the uploaded PDFs. Must use either pink, orange, lime green, white, or black. We prefer a bright pink background with white lettering as our first choice, but are willing to be open minded to see all creative concepts. Also the sign is 14 feet long and 42 inches tall so the artwork must fit within those boundaries. Also keep in mind the sign does have a 4 inch black frame. So the graphics area is actually 13 feet 2 inches by 3 feet. Also, in the attached pdf that shows a rough possible layout, the words "101 cakes to go" is on the sign. It is NOT a must. Only use the wording if it adds to your design.
Nice to have
• You are welcome to add additional stars or other fun graphics that could look good.
Should not have
• No images of cakes or other bakery products.

```html
<!DOCTYPE html>
<html lang="en">
<head>
<meta charset="utf-8">
<title>The Willow Lantern — Sign Face</title>
<link href="https://fonts.googleapis.com/css2?family=Fredoka:wght@600&display=swap" rel="stylesheet">
<style>
  :root {
    --pink: #ff6eb8;
    --pink-pale: #fcc3e2;
    --lime: #caff7d;
    --orange: #ffb95c;
    --white: #ffffff;
  }
  html, body {
    margin: 0;
    padding: 0;
    width: 1200px;
    height: 270px;
    overflow: hidden;
    background: var(--pink);
  }
  .sign-face {
    position: relative;
    width: 1200px;
    height: 270px;
    overflow: hidden;
    background: var(--pink);
  }
  .sign-shapes {
    position: absolute;
    inset: 0;
    display: block;
  }
  .shape-lime { fill: var(--lime); }
  .shape-orange { fill: var(--orange); }
  .shape-pink { fill: var(--pink); }
  .star-field { fill: var(--pink); }
  .brand-name {
    position: absolute;
    left: 0;
    right: 0;
    top: 78px;
    margin: 0;
    text-align: center;
    font-family: "Fredoka", "Arial Rounded MT Bold", sans-serif;
    font-weight: 600;
    font-size: 58px;
    line-height: 1;
    letter-spacing: 0.5px;
    color: var(--white);
  }
</style>
</head>
<body>
  <div class="sign-face">
    <svg class="sign-shapes" width="1200" height="270" viewBox="0 0 1200 270" aria-hidden="false">
      <!-- left corner blobs -->
      <path class="shape-orange" d="M0,180 L250,170 C275,215 295,250 326,270 L0,270 Z"/>
      <path class="shape-lime" d="M0,47 C45,40 80,18 93,0 L274,0 C280,50 290,120 278,150 C262,190 215,215 160,240 C130,254 112,262 100,270 L0,270 Z"/>
      <!-- right corner blobs -->
      <path class="shape-orange" d="M870,0 L1000,0 L1000,140 C960,130 915,112 885,95 C845,72 835,40 870,0 Z"/>
      <path class="shape-lime" d="M1003,0 L1200,0 L1200,270 L965,270 C955,230 948,170 941,120 C935,70 950,35 1003,0 Z"/>
      <path class="shape-pink" d="M1085,270 C1115,235 1150,180 1200,163 L1200,270 Z"/>
      <!-- scattered star pattern area -->
      <rect class="star-field" x="278" y="0" width="592" height="270" fill-opacity="0" role="img" aria-label="Scattered pale pink hand-drawn stars across the pink background"/>
    </svg>
    <h1 class="brand-name">The Willow Lantern</h1>
  </div>
</body>
</html>
```